First Website for Meridian Advisory Collective

We need a great new website design to flow with our brand identity (attached; developed here on ArtHive just recently). It needs to be professional, but with just a little bit of fun thrown in, to reflect the caribbean location of our business. The logo already achieves this and thus it should flow from there.

The site will have a few primary sections:

Home - self explanatory, and overview of our business and some of the most recent posts from the next section
Notes - Really just a fancy word for a blog, it will be an ordered set of posts on various regulatory and business news items relevant to Caribbean businesses
"Start/Relocate a Consulting Practice?" or "Become a Partner" - A section on how to bring a consulting practice, new or old, into the partnership and the tax and regulatory advantages of doing so
Contact - Self explanatory

So, it needs a navigation that supports that sparse set of top level links, and a basic design for home, one interior page like "Become a Partner", and the blog/Notes section, that my developer can work from.

UPDATE: I like the designs that have brought in the logo colors to make each sub-page uniquely colored. But, all so far rely too heavily on smiling photos of people. 1) Notes will not have photos to go with them (this is going to be mostly legal updates, tax info, etc.) 2) For the hero photon on the home page, it shouldn't be too high, and should probably be a photo of a beach, preferably one from Puerto Rico where we are located. 3) There should be no search and no social media buttons - the design is meant to be sparse on purpose and we have no need for those items.

Other than the logo, please stick to web safe or google web fonts for text, and have them specified in the source format during delivery. Thanks.

Target Market(s)

Business owners. Often in high tech fields. As well as high net worth family offices.

Industry/Entity Type

Legal

Requirements
Must have
• Must pull in colors from the logo effectively, without looking garish or overly bright.

```html
<!DOCTYPE html>
<html lang="en">
<head>
<meta charset="utf-8">
<title>Blog – Meridian Advisory Collective</title>
<link rel="stylesheet" href="https://fonts.googleapis.com/css2?family=Open+Sans:wght@400;600;700&family=Roboto+Condensed:wght@300;400&display=swap">
<style>
  :root {
    --page-bg: #ebebeb;
    --sheet: #ffffff;
    --header-bg: #f3f3f3;
    --brand-red: #c8202f;
    --brand-blue: #29a9e1;
    --brand-green: #27b36f;
    --ink: #111111;
    --body-text: #7a7a7a;
    --rule: #e2e2e2;
    --footer-bg: #2b2a2a;
    --footer-text: #ffffff;
  }
  * { box-sizing: border-box; margin: 0; padding: 0; }
  html, body { width: 1020px; height: 1200px; overflow: hidden; }
  body { background: var(--page-bg); font-family: "Roboto Condensed", "Arial Narrow", sans-serif; position: relative; }

  .sheet { position: absolute; left: 87px; top: 0; width: 846px; height: 1200px; background: var(--sheet); }

  .site-header { position: absolute; left: 0; top: 0; width: 846px; height: 84px; background: var(--header-bg); }
  .brand { position: absolute; left: 13px; top: 29px; display: flex; align-items: center; gap: 9px;
    font-family: "Open Sans", sans-serif; font-weight: 700; font-size: 19px; color: var(--brand-red); letter-spacing: -0.2px; }
  .brand-mark { width: 14px; height: 14px; background: var(--brand-red); }

  .main-nav { position: absolute; top: 0; height: 84px; left: 0; width: 846px; }
  .main-nav a { position: absolute; top: 0; height: 84px; line-height: 84px; font-family: "Open Sans", sans-serif;
    font-size: 9px; font-weight: 600; color: var(--ink); text-decoration: none; transform: translateX(-50%); white-space: nowrap; }
  .main-nav a.is-active { background: var(--brand-red); color: #fff; width: 52px; text-align: center; }

  .page-band { position: absolute; left: 0; top: 129px; width: 846px; height: 35px; background: var(--brand-blue); }
  .page-band h1 { position: absolute; left: 89px; top: 4px; font-weight: 400; font-size: 22px; color: #fff; letter-spacing: 0.3px; }
  .band-shadow { position: absolute; left: 26px; top: 164px; width: 794px; height: 18px; }

  .feature-photo { position: absolute; left: 86px; top: 215px; width: 265px; height: 166px; border: 4px solid #d9d9d9;
    box-shadow: 0 1px 3px rgba(0,0,0,.25);
    background: linear-gradient(180deg, #c7a2a6 0%, #e6b79a 30%, #7d8fa8 52%, #1f4e7a 62%, #163e64 100%); }

  .post-title { position: absolute; left: 372px; top: 214px; font-weight: 400; font-size: 22px; color: var(--ink); }
  .copy { position: absolute; font-weight: 300; font-size: 9.3px; line-height: 17.3px; color: var(--body-text); text-align: justify; }
  .copy p + p { margin-top: 7px; }
  .post-intro { left: 372px; top: 246px; width: 368px; }
  .side-copy { left: 93px; top: 410px; width: 248px; }

  .accordion-item { position: absolute; left: 376px; height: 38px; border: 1px solid var(--rule); display: flex; align-items: center; }
  .accordion-toggle { width: 47px; height: 38px; margin: -1px 0 -1px -1px; display: flex; align-items: center; justify-content: center;
    background: var(--brand-blue); color: #fff; font-family: "Open Sans", sans-serif; font-weight: 700; font-size: 16px; }
  .accordion-item.is-open .accordion-toggle { width: 66px; background: var(--brand-green); }
  .accordion-label { font-weight: 300; font-size: 9.5px; color: var(--body-text); padding-left: 20px; }
  .accordion-item.is-open .accordion-label { padding-left: 8px; font-size: 10px; }
  .accordion-panel { left: 440px; top: 472px; width: 260px; }

  .site-footer { position: absolute; left: 0; top: 1144px; width: 846px; height: 56px; background: var(--footer-bg); }
  .site-footer a { position: absolute; top: 0; line-height: 56px; transform: translateX(-50%); font-family: "Open Sans", sans-serif;
    font-size: 8.5px; color: var(--footer-text); text-decoration: none; white-space: nowrap; }
</style>
</head>
<body>
<div class="sheet">
  <header class="site-header">
    <div class="brand"><span class="brand-mark"></span>Meridian Advisory Collective</div>
    <nav class="main-nav">
      <a class="is-active" href="#" style="left:467px">HOME</a>
      <a href="#" style="left:532px">ABOUT US</a>
      <a href="#" style="left:601px">BLOG</a>
      <a href="#" style="left:686px">BECOME A PARTNER</a>
      <a href="#" style="left:782px">CONTACT US</a>
    </nav>
  </header>

  <div class="page-band"><h1>BLOG</h1></div>
  <svg class="band-shadow" viewBox="0 0 794 18" aria-hidden="true">
    <path d="M0 0 H794 L790 14 Q397 4 4 14 Z" fill="#000"/>
  </svg>

  <div class="feature-photo" role="img" aria-label="Stone sentry box on a seaside fortress wall at sunset over the ocean"></div>

  <h2 class="post-title">Lorem ipsum dolor</h2>
  <div class="copy post-intro">
    <p>Lorem ipsum dolor sit amet, consectetur adipisicing elit, sed do eiusmod tempor incididunt ut labore et dolore magna aliqua. Ut enim ad minim veniam, quis nostrud exercitation ullamco ipsum dolor sit amet, consectetur adipisicing elit, sed do eiusmod tempor incididunt ut labore et dolore magna aliqua. Ut enim ad minim veniam, quis nostrud exercitation ullamco sed do eiusmod tempor incididunt ut labore et dolore magna aliqua. Ut enim ad minim veniam, quis nostrud exercitation ullamco .</p>
  </div>

  <div class="copy side-copy">
    <p>Lorem ipsum dolor sit amet, consectetur adipisicing elit, sed do eiusmod tempor incididunt ut labore et dolore magna aliqua. Ut enim ad minim veniam, quis nostrud exercitation ullamco ipsum dolor sit amet, consectetur adipisicing elit, sed do eiusmod tempor incididunt ut labore et dolore magna aliqua. Ut enim ad minim veniam, quis nostrud exercitation ullamco .</p>
    <p>Lorem ipsum dolor sit amet, consectetur adipisicing elit, sed do eiusmod tempor incididunt ut labore et dolore magna aliqua. Ut enim ad minim veniam, quis nostrud exercitation ullamco ipsum dolor sit amet, consectetur adipisicing elit, sed do eiusmod tempor incididunt ut labore et dolore magna aliqua.</p>
  </div>

  <div class="accordion-item is-open" style="top:419px;width:360px">
    <span class="accordion-toggle">+</span><span class="accordion-label">Lorem ipsum dolor sit amet, consectetur adipisicing elit.</span>
  </div>
  <div class="copy accordion-panel">
    <p>Lorem ipsum dolor sit amet, consectetur adipisicing elit, sed do eiusmod tempor incididunt ut labore et dolore magna aliqua. Ut enim ad minim veniam, quis nostrud exercitation ullamco ipsum dolor sit amet, consectetur adipisicing elit, sed do eiusmod tempor incididunt ut labore et dolore magna aliqua. Ut enim ad minim veniam, quis nostrud exercitation ullamco .</p>
  </div>
  <div class="accordion-item" style="top:599px;width:366px">
    <span class="accordion-toggle">+</span><span class="accordion-label">Lorem ipsum dolor sit amet, consectetur adipisicing elit, sed do eiusmod.</span>
  </div>
  <div class="accordion-item" style="top:652px;width:366px">
    <span class="accordion-toggle">+</span><span class="accordion-label">Lorem ipsum dolor sit amet, consectetur adipisicing elit, sed do eiusmod.</span>
  </div>

  <footer class="site-footer">
    <a href="#" style="left:258px">HOME</a>
    <a href="#" style="left:322px">ABOUT US</a>
    <a href="#" style="left:392px">BLOG</a>
    <a href="#" style="left:477px">BECOME A PARTNER</a>
    <a href="#" style="left:573px">CONTACT US</a>
  </footer>
</div>
</body>
</html>
```